Women's Empowerment & Prayer Brunch - Matching Poster, flyer and Postcard

We are a Christian Event & Travel Company and we are hosting our inaugural event on June 10, 2017. This event is a women's empowerment & prayer brunch aboard a private yacht leaving out of Bayview Landing, Maryland. The event will cater to women who have a vision to start or have already embarked on the journey of starting or growing a business or ministry. The event calls for a matching poster, flyer and postcard design that give an elegant & exquisite feel with just the right breath of freshness. The colors should reflect our logo as this is our launch event. I have also included 2 photos of the Coralwind Heritage Village production (one of our sponsors) - Please include but do not make it take over the design - this is to advertise the door prize. The final design will portray the branding of the company (Christian, travel, events, elegance, professional), the branding of the event (elegant and luxurious) and the importance of this launch event.
Please include the following information:
Brightfold Event & Travel Group presents
Event name: Rising Through Storms: Grace, Devotion & Service.
Tag Line/Description: An Exquisite Women's Empowerment & Prayer Brunch.
Guest Speaker: Minister Lorraine T. Maddox (Photo included)
VP of Trellmont Bank
Asst. Pastor & First Lady of Greenvale Baptist Church
Special Guest Psalmist: Minister Tasha Morrow (Photo Included)
Worship Director of Stonebrook Community Church
Vocalist, Songwriter, Musician, and Clinician
Venue: Aboard the Silver Crest Yacht
Dock: Bayview Landing
472 Gull Point Way, Ferndale, MD 20893
Boarding 10:00am
Sailing Promptly at 10:30am
(Please be on time the yacht will not wait)
Date: Saturday June 10, 2017
Tickets: Early Bird US$75.00/person (ends May 15, 2017)
Regular Tickets US$95.99
Purchase Tickets at www.brightfoldevent-travel.example/rising-through-storms
SPACE IS LIMITED DUE TO YACHT CAPACITY
Grand Prize: Adrian Vell Purse
Door Prize: 2 Tickets to the Island Coralwind Heritage Village
Other prizes for special ladies in attendance.
Ladies are asked to dress in Elegant White Ensemble
Corporate Sponsors:
The Coralwind Heritage Village (Logo included)
J. Ransom Photography (Logo included)
Special Thanks to our Individual Sponsors:
Mrs. K. Lyle, Mr. G Farris & Mr. R. Danby

Target Market(s)

Women, Business, Ministry, Christians, Middle to Upper Class

Industry/Entity Type

Events

Font styles to use
Serif
Script

Requirements
Must have
• Elegance, professional, vivid in color & font. be creative in Visual and FONT!
• Poster: 18" X 24"
• Flyer: one sided.
• ***** the final design chosen will have a cross referenced design of 1 flyer, 1 postcard 1 poster. This was included so you have a reference - Be creative!!!!!!
Nice to have
• Matching across all 3 designs (poster, flyer & postcard) but sized appropriately and just enough difference to play up the design and be appealing.
• I uploaded 3 example flyers to give you inspiration of the type of visuals I'm looking for. I removed my amateur sample because the designs were copying it instead of being creative.
Should not have
• Any thing inappropriate, alcohol oriented or sexual

```html
<!DOCTYPE html>
<html lang="en">
<head>
<meta charset="utf-8">
<title>Rising Through Storms – Women's Empowerment &amp; Prayer Brunch</title>
<link href="https://fonts.googleapis.com/css2?family=Pinyon+Script&family=Cinzel:wght@400;600&family=Playfair+Display:ital,wght@1,400;1,600&family=Arimo:wght@400;700&display=swap" rel="stylesheet">
<style>
:root{
  --sky-deep:#1459b3;
  --sky-mid:#3d8fd6;
  --sky-light:#8fc6ea;
  --sea-top:#9ccfe6;
  --gold:#e9b824;
  --white:#ffffff;
  --link:#0c3f8f;
}
*{margin:0;padding:0;box-sizing:border-box}
html,body{width:962px;height:1200px;overflow:hidden;background:#fff}
.poster{
  position:relative;width:962px;height:1200px;overflow:hidden;
  background:linear-gradient(180deg,var(--sky-deep) 0%,#1c6cc2 28%,var(--sky-mid) 48%,var(--sky-light) 72%,var(--sea-top) 100%);
  color:var(--white);font-family:"Arimo",Arial,sans-serif;
}
.sea{
  position:absolute;left:0;right:0;top:890px;bottom:0;
  background:linear-gradient(180deg,#a9d5ea 0%,#7dbcd6 6%,#8cc3d9 40%,#a3cfe0 100%);
}
.abs{position:absolute}
.center{left:0;right:0;text-align:center}

.brand{top:34px;display:flex;justify-content:center;align-items:center;gap:12px}
.brand-dot{width:16px;height:16px;border-radius:50%;background:var(--gold)}
.brand-name{font-family:"Cinzel",serif;font-weight:600;font-size:20px;letter-spacing:2px;color:var(--gold)}
.presents{top:96px;font-family:"Playfair Display",serif;font-style:italic;font-size:17px}
.title{top:112px;font-family:"Pinyon Script",cursive;font-size:96px;line-height:1.2;font-weight:400}

.theme-band{top:252px;left:20px;right:20px;height:62px;border-top:2px solid var(--white);border-bottom:2px solid var(--white);display:flex;align-items:center;justify-content:center}
.theme{font-family:"Cinzel",serif;font-weight:600;font-size:22px;letter-spacing:6px;color:var(--gold)}
.tagline{top:332px;font-family:"Cinzel",serif;font-size:15px;letter-spacing:3px}
.date{top:360px;font-family:"Cinzel",serif;font-weight:600;font-size:28px;letter-spacing:5px;color:var(--gold)}

.portrait{position:absolute;width:150px;height:186px;border-radius:50%;border:5px solid var(--gold);top:420px}
.portrait.speaker{left:258px;background:radial-gradient(ellipse at 50% 60%,#c33a2e 0%,#7a2a22 55%,#3b1b14 100%)}
.portrait.guest{left:554px;background:radial-gradient(ellipse at 50% 65%,#f1ede6 0%,#6b5a4e 45%,#1d1a18 100%)}

.role{font-family:"Playfair Display",serif;font-style:italic;font-weight:600;font-size:22px;margin-bottom:10px}
.person{font-size:15px;line-height:1.3}
.person b{font-size:16px}
.person p{margin-bottom:14px}
.speaker-text{top:430px;right:712px;width:230px;text-align:right}
.guest-text{top:418px;left:724px;width:230px}

.details{top:630px;left:40px;right:40px;height:180px}
.col{position:absolute;top:0}
.col-dock{right:608px;width:300px;text-align:right}
.col-time{left:380px;width:260px;text-align:center}
.col-tix{left:656px;width:220px}
.rule-v{position:absolute;top:0;width:1.5px;height:172px;background:var(--white)}
.rule-v.one{left:370px}.rule-v.two{left:646px}
.h{font-family:"Playfair Display",serif;font-style:italic;font-weight:600;font-size:20px}
.t{font-size:16px;line-height:1.3}
.note{font-family:"Playfair Display",serif;font-style:italic;font-weight:600;font-size:19px;line-height:1.3;margin-top:16px}
.col-time .note{font-size:18px}
.col-tix .t b{font-size:16px}
.col-tix .small{font-family:"Playfair Display",serif;font-style:italic;font-size:14px;padding-left:60px}

.purchase{top:830px;font-family:"Playfair Display",serif;font-style:italic;font-weight:600;font-size:21px}
.url{top:860px;font-size:19px;color:var(--link)}
.rule-h{position:absolute;height:1.5px;background:var(--white)}
.rule-a{top:892px;left:355px;width:252px}
.limited{top:902px;font-weight:700;font-size:19px;letter-spacing:1px}

.badge{position:absolute;width:92px;height:92px;border-radius:50%;background:var(--gold);border:4px solid var(--white);display:flex;align-items:center;justify-content:center;text-align:center;font-family:"Cinzel",serif;font-weight:600;font-size:15px;line-height:1.1;color:var(--white);transform:rotate(-18deg)}
.badge.grand{left:200px;top:948px}
.badge.door{left:558px;top:940px}
.prize-grand{left:312px;top:954px;font-family:"Playfair Display",serif;font-style:italic;font-size:28px;line-height:1.25}
.prize-door{left:668px;top:948px;font-family:"Playfair Display",serif;font-style:italic;font-size:16px;line-height:1.3}
.others{top:1048px;font-family:"Playfair Display",serif;font-style:italic;font-size:16px}
.rule-b{top:1078px;left:345px;width:270px}

.sponsors{top:1094px;left:100px;right:40px;display:flex;align-items:center;justify-content:center;gap:36px}
.sponsors-label{font-family:"Cinzel",serif;font-weight:600;font-size:22px;letter-spacing:4px;color:var(--gold);line-height:1.15;text-align:center}
.sponsor-name{font-family:"Cinzel",serif;font-weight:600;font-size:16px;letter-spacing:0.5px;color:var(--white);white-space:nowrap}
.thanks{top:1146px;font-family:"Playfair Display",serif;font-style:italic;font-weight:600;font-size:16px}
.individuals{top:1170px;font-size:19px}
</style>
</head>
<body>
<main class="poster">
  <div class="sea" role="img" aria-label="Photograph of a calm turquoise sea under a pale sky"></div>

  <div class="abs center brand"><span class="brand-dot"></span><span class="brand-name">Brightfold Event &amp; Travel Group</span></div>
  <div class="abs center presents">presents</div>
  <h1 class="abs center title">Rising Through Storms</h1>
  <div class="abs theme-band"><span class="theme">GRACE, DEVOTION &amp; SERVICE</span></div>
  <div class="abs center tagline">AN EXQUISITE WOMEN'S EMPOWERMENT &amp; PRAYER BRUNCH</div>
  <div class="abs center date">SATURDAY, JUNE 10, 2017</div>

  <div class="portrait speaker" role="img" aria-label="Portrait of guest speaker Minister Lorraine T. Maddox"></div>
  <div class="portrait guest" role="img" aria-label="Portrait of special guest Minister Tasha Morrow"></div>

  <div class="abs speaker-text">
    <div class="role">Guest Speaker</div>
    <div class="person">
      <p>Minister<br><b>Lorraine T. Maddox</b></p>
      <p>VP of Trellmont Bank</p>
      <p>Asst. Pastor &amp; First Lady of<br>Greenvale Baptist Church</p>
    </div>
  </div>
  <div class="abs guest-text">
    <div class="role">Special Guest</div>
    <div class="person">
      <p>Minister<br><b>Tasha Morrow</b></p>
      <p>Worship Director of<br>Stonebrook Community Church</p>
      <p>Vocalist, Songwriter,<br>Musician, and Clinician</p>
    </div>
  </div>

  <section class="abs details">
    <div class="rule-v one"></div><div class="rule-v two"></div>
    <div class="col col-dock">
      <div class="h">Dock:</div>
      <div class="t" style="margin-top:10px">Bayview Landing<br>472 Gull Point Way<br>Ferndale, MD 20893</div>
      <div class="note">Ladies are asked to dress<br>in Elegant White Ensemble</div>
    </div>
    <div class="col col-time">
      <div class="h">Boarding:</div>
      <div class="t">10:00am</div>
      <div class="h" style="margin-top:10px">Sailing Promptly at:</div>
      <div class="t">10:30am</div>
      <div class="note">(Please be on time,<br>the yacht will not wait)</div>
    </div>
    <div class="col col-tix">
      <div class="h">Tickets:</div>
      <div class="t" style="margin-top:10px"><b>Early Bird:</b><br>US$75.00/person</div>
      <div class="small">(ends May 15, 2017)</div>
      <div class="t" style="margin-top:12px"><b>Regular Tickets:</b><br>US$95.99</div>
    </div>
  </section>

  <div class="abs center purchase">Purchase Tickets at:</div>
  <div class="abs center url">www.brightfoldevent-travel.example/rising-through-storms/</div>
  <div class="rule-h rule-a"></div>
  <div class="abs center limited">SPACE IS LIMITED DUE TO YACHT CAPACITY</div>

  <div class="badge grand">GRAND<br>PRIZE</div>
  <div class="abs prize-grand">Adrian Vell<br>Purse</div>
  <div class="badge door">DOOR<br>PRIZE</div>
  <div class="abs prize-door">2 Tickets<br>to the Island Coralwind<br>Heritage Village</div>
  <div class="abs center others">Other prizes for special ladies in attendance.</div>
  <div class="rule-h rule-b"></div>

  <div class="abs sponsors">
    <div class="sponsors-label">CORPORATE<br>SPONSORS</div>
    <div class="sponsor-name">J. Ransom Photography</div>
    <div class="sponsor-name">Coralwind Heritage Village</div>
  </div>
  <div class="abs center thanks">Special Thanks to our Individual Sponsors:</div>
  <div class="abs center individuals">Mrs. K. Lyle, Mr. G Farris &amp; Mr. R. Danby</div>
</main>
</body>
</html>
```